Visitenkarten-Design für Autowerkstatt/-verwertung
Zielgruppe
Unser Unternehmen besteht aus zwei Bereiche:
- Autoverwertung
- Autowerkstatt
Aufgabenstellung
Informationen auf der Visitenkarte:
'Brunnhofer' - Logo
Lindenauer Str. 31
80993 München
Autoverwertung Autoteile
www.autoverwertung-brunnhofer-beispiel.de
info@autoverwertung-brunnhofer-beispiel.de
Autowerkstatt
www.auto-brunnhofer-beispiel.de
info@auto-brunnhofer-beispiel.de
Öffnungszeiten:
Mo-Fr
08.00 - 12.00 Uhr und 13.00 - 17.00 Uhr
Farblich sollte die Visitenkarte sich an das Logo anpassen. Visitenkarte 2-4 seitig.

```html
<!DOCTYPE html>
<html lang="de">
<head>
<meta charset="utf-8">
<title>Visitenkarte Brunnhofer</title>
<link href="https://fonts.googleapis.com/css2?family=Noto+Sans:wght@400;700&family=Poppins:wght@300&display=swap" rel="stylesheet">
<style>
:root{
  --red:#c0261c;
  --black:#1d1d1b;
  --grey:#ececec;
  --line:#c9c9c9;
  --white:#fff;
  --text:#1d1d1b;
  --photo-a:#6d6a6a;
  --photo-b:#a9a9a9;
}
*{margin:0;padding:0;box-sizing:border-box}
html,body{width:1200px;height:800px;overflow:hidden;background:var(--white)}
body{position:relative;font-family:"Noto Sans",Verdana,sans-serif;color:var(--text)}
.caption{position:absolute;font-family:"Poppins",Arial,sans-serif;font-weight:300;font-size:20px;letter-spacing:-.5px;text-align:center;transform:translateX(-50%);white-space:nowrap}
.card{position:absolute;box-shadow:2px 3px 6px rgba(0,0,0,.25)}
.info{position:absolute;left:0;right:0;text-align:center;font-size:14px;line-height:16.5px}
.info .head{color:var(--red);font-weight:700}
.info .phone{margin-top:7px;display:inline-flex;align-items:center;gap:6px}
.phone svg{width:15px;height:11px}
.photo{position:absolute;background:linear-gradient(90deg,var(--photo-a),var(--photo-b))}

.card-open{left:118px;top:132px;width:409px;height:268px;background:var(--grey)}
.card-open .photo{left:0;right:0;top:106px;height:52px}
.card-open .info{top:168px}
.flap{position:absolute;left:118px;top:132px;width:562px;height:148px;overflow:visible}
.flap-text{position:absolute;left:238px;top:168px;width:300px;text-align:center}
.brand{font-weight:700;font-size:28px;color:var(--black);line-height:30px;display:inline-flex;align-items:center;gap:8px}
.brand .mark{width:14px;height:14px;border-radius:50%;background:var(--red)}
.tagline{color:var(--red);font-size:7px;font-weight:700;border-top:2px solid var(--red);margin:1px 14px 0 40px;line-height:9px}
.address{font-size:12px;line-height:13px;margin-top:6px}

.card-back{left:118px;top:476px;width:409px;height:270px;background:var(--red);box-shadow:none}
.map{position:absolute;left:57px;top:23px;width:294px;height:218px;background:linear-gradient(135deg,#f7f7f7,#dcdcdc)}

.card-inner{left:729px;top:56px;width:408px;height:538px;background:var(--grey)}
.hours{position:absolute;left:0;top:0;width:408px;height:270px;background:var(--white);border-bottom:2px solid var(--line);text-align:center;font-size:14px;line-height:16.3px;padding-top:82px}
.hours .title{font-weight:700;margin-bottom:19px}
.card-inner .info-parts{top:292px}
.card-inner .photo-a{left:0;top:377px;width:197px;height:52px}
.card-inner .photo-b{left:209px;top:377px;width:199px;height:52px;background:linear-gradient(90deg,var(--photo-b),var(--photo-a))}
.card-inner .band{position:absolute;left:0;right:0;top:374px;height:58px;border-top:2px solid var(--line);border-bottom:2px solid var(--line)}
.card-inner .info-shop{top:438px}
</style>
</head>
<body>
<div class="caption" style="left:323px;top:74px">Aufgeklappte Karte</div>

<div class="card card-open">
  <div class="photo" role="img" aria-label="Foto: Mechaniker an einem Autorad und Autoersatzteile"></div>
  <div class="info">
    <div class="head">Autowerkstatt</div>
    <div>www.auto-brunnhofer-beispiel.de</div>
    <div>info@auto-brunnhofer-beispiel.de</div>
    <div class="phone"><svg viewBox="0 0 15 11"><path d="M1 3q6.5-4 13 0v2h-3V3.5H4V5H1z M3 5h9l2 5H1z" fill="#1d1d1b"/></svg>0160 - 00 12 34 5</div>
  </div>
</div>

<svg class="flap" viewBox="0 0 562 148">
  <defs>
    <clipPath id="flapShape"><polygon points="0,0 426,0 560,146 136,146"/></clipPath>
    <filter id="flapShadow"><feDropShadow dx="3" dy="4" stdDeviation="3" flood-opacity=".3"/></filter>
  </defs>
  <polygon points="0,0 426,0 560,146 136,146" fill="#fff" filter="url(#flapShadow)"/>
  <g clip-path="url(#flapShape)">
    <rect x="0" y="0" width="562" height="16" fill="#c0261c"/>
    <rect x="0" y="118" width="562" height="30" fill="#1d1d1b"/>
  </g>
</svg>
<div class="flap-text">
  <div class="brand"><span class="mark"></span>Brunnhofer</div>
  <div class="tagline">Autoverwertung · Autoteile · Autohandel · Autowerkstatt</div>
  <div class="address">Lindenauer Straße 31<br>80993 München</div>
</div>

<div class="caption" style="left:323px;top:440px">Rückseite zugeklappte Karte</div>
<div class="card card-back">
  <div class="map" role="img" aria-label="Anfahrtsskizze mit Straßenplan und Standortmarkierung"></div>
</div>

<div class="card card-inner">
  <div class="hours">
    <div class="title">Öffnungszeiten:</div>
    <div>Mo-Fr</div>
    <div>08.00 - 12.00 Uhr</div>
    <div>und</div>
    <div>13.00 - 17.00 Uhr</div>
  </div>
  <div class="info info-parts">
    <div class="head">Autoverwertung Autoteile</div>
    <div>www.autoverwertung-brunnhofer-beispiel.de</div>
    <div>info@autoverwertung-brunnhofer-beispiel.de</div>
    <div class="phone"><svg viewBox="0 0 15 11"><path d="M1 3q6.5-4 13 0v2h-3V3.5H4V5H1z M3 5h9l2 5H1z" fill="#1d1d1b"/></svg>089 - 00 98 76 54</div>
  </div>
  <div class="band"></div>
  <div class="photo photo-a" role="img" aria-label="Foto: Mechaniker an einem Autorad"></div>
  <div class="photo photo-b" role="img" aria-label="Foto: Autoersatzteile wie Zahnriemen und Rollen"></div>
  <div class="info info-shop">
    <div class="head">Autowerkstatt</div>
    <div>www.auto-brunnhofer-beispiel.de</div>
    <div>info@auto-brunnhofer-beispiel.de</div>
    <div class="phone"><svg viewBox="0 0 15 11"><path d="M1 3q6.5-4 13 0v2h-3V3.5H4V5H1z M3 5h9l2 5H1z" fill="#1d1d1b"/></svg>0160 - 00 12 34 5</div>
  </div>
</div>
<div class="caption" style="left:933px;top:626px">Innenteil aufgeklappte Karte</div>
</body>
</html>
```